Flyer Design Project

We want to design a flyer for a laundromat in San Francisco. It will be used to market the services of the laundromat. I am uploading a .jpg file with details to be highlighted. The flyer should be of size 8.5 in x 11 in and should be attractive and hard hitting. The attachment should only be used for the copy, not for design.

Target Market(s)

Laundromat and laundry users

Requirements
Must have
• Must have a attention grabbing headline
Nice to have
• Pictures

```html
<!DOCTYPE html>
<html lang="en">
<head>
<meta charset="utf-8">
<title>Marlowe Laundromat Flyer</title>
<link href="https://fonts.googleapis.com/css2?family=Anton&family=Oswald:wght@500&family=Lato:wght@400;700;900&display=swap" rel="stylesheet">
<style>
:root{
  --navy:#1d3f7c;
  --mid-blue:#1a6fc0;
  --sky:#2aa3e6;
  --deep-sky:#0f6fb8;
  --red:#e3262d;
  --orange:#f7a21b;
  --white:#ffffff;
  --lime:#9acd3b;
  --photo-warm:#c9b79a;
  --photo-cool:#b9c2c6;
}
*{margin:0;padding:0;box-sizing:border-box}
html,body{width:1200px;height:927px;overflow:hidden;background:var(--white)}
body{position:relative;font-family:"Lato",sans-serif}

.front{position:absolute;left:45px;top:78px;width:548px;height:708px;overflow:hidden;background:var(--navy)}
.hero-photo{position:absolute;left:0;top:0;width:548px;height:450px;
  background:linear-gradient(160deg,#7f9a86 0%,#d8d3c6 35%,var(--photo-warm) 60%,#9fb0b6 100%)}
.hero-wave{position:absolute;left:0;top:250px;width:548px;height:200px}
.offer{position:absolute;left:40px;top:262px;display:flex;align-items:flex-end;line-height:1}
.offer-num{font-family:"Anton",sans-serif;font-size:136px;color:var(--red);
  -webkit-text-stroke:4px var(--white);paint-order:stroke fill;letter-spacing:-2px}
.offer-word{font-family:"Oswald",sans-serif;font-size:128px;color:var(--white);
  -webkit-text-stroke:3px var(--red);letter-spacing:-4px;margin-left:4px;margin-bottom:4px}
.offer-sub{position:absolute;left:44px;top:403px;font-size:27px;color:var(--white);letter-spacing:.2px}
.interior-a{position:absolute;left:0;top:450px;width:274px;height:152px;
  background:linear-gradient(180deg,#b8bcbd 0%,#8f9596 55%,#3c3c3c 100%)}
.interior-b{position:absolute;left:274px;top:450px;width:274px;height:152px;
  background:linear-gradient(180deg,var(--photo-cool) 0%,#e7eaea 60%,#cfd6d8 100%)}
.brand-bar{position:absolute;left:0;top:602px;width:275px;height:106px;background:var(--navy);
  display:flex;align-items:center;padding-left:30px;gap:16px}
.brand-dot{width:60px;height:60px;border-radius:50%;background:#c7ccd3}
.brand-name{font-size:24px;font-weight:400;color:var(--white);line-height:1.1}
.contact{position:absolute;left:275px;top:602px;width:273px;height:106px;background:var(--mid-blue);
  padding:10px 0 0 15px;color:var(--white);font-size:13.5px;line-height:1.4}
.contact strong{font-weight:700}

.back{position:absolute;left:622px;top:78px;width:548px;height:710px;overflow:hidden;
  background:radial-gradient(circle at 60% 50%,#1e88d4 0%,var(--sky) 60%,#39b1ee 100%)}
.back-decor{position:absolute;left:0;top:0;width:548px;height:710px}
.perks{position:absolute;left:21px;top:24px;list-style:none}
.perk{position:relative;display:flex;height:93px}
.perk-tab{width:62px;height:80px;border-top:10px solid #333;display:flex;align-items:center;justify-content:center;flex:none}
.perk-tab svg{width:50px;height:50px}
.perk-copy{margin-left:9px;padding-top:14px;width:445px}
.perk-title{font-size:16px;font-weight:900;color:var(--orange);text-transform:uppercase;letter-spacing:.3px;line-height:1.05;text-shadow:1px 1px 1px rgba(0,0,0,.35)}
.perk-text{font-size:12.5px;color:var(--white);line-height:1.35;margin-top:2px}
.back-url{position:absolute;left:140px;top:674px;font-size:17px;font-weight:700;color:var(--white)}
</style>
</head>
<body>

<section class="front">
  <div class="hero-photo" role="img" aria-label="Smiling couple holding laundry in front of front-loading washers"></div>
  <svg class="hero-wave" viewBox="0 0 548 200" preserveAspectRatio="none">
    <path d="M0 60 Q200 40 360 20 T548 0 V200 H0Z" fill="#2386d2"/>
    <path d="M0 110 Q250 70 548 40 V200 H0Z" fill="#1458a8"/>
    <circle cx="30" cy="40" r="20" fill="#3fb4ea" opacity=".7"/>
    <circle cx="470" cy="20" r="24" fill="#3fb4ea" opacity=".6"/>
    <circle cx="420" cy="50" r="10" fill="#3fb4ea" opacity=".6"/>
  </svg>
  <div class="offer"><span class="offer-num">50</span><span class="offer-word">%OFF</span></div>
  <p class="offer-sub">On your first wash and fold order!</p>
  <div class="interior-a" role="img" aria-label="Laundromat interior with stainless washers and checkered floor"></div>
  <div class="interior-b" role="img" aria-label="Bright laundromat row of white washers and dryers"></div>
  <div class="brand-bar"><span class="brand-dot"></span><span class="brand-name">Marlowe<br>Laundromat</span></div>
  <div class="contact">
    2817 Larkspur St, San Francisco,<br>CA 94109 (Next to GreenCart Market)<br>www.marlowelaundromat.com<br>415.555.0142<br><strong>Open Every Day from 6am to 10pm</strong>
  </div>
</section>

<section class="back">
  <svg class="back-decor" viewBox="0 0 548 710">
    <rect x="0" y="50" width="548" height="95" fill="#1b7cc7" opacity=".5"/>
    <circle cx="320" cy="420" r="250" fill="none" stroke="#1a78c4" stroke-width="60" opacity=".5"/>
    <circle cx="480" cy="110" r="40" fill="#3fc0f2" opacity=".6"/>
    <circle cx="350" cy="30" r="16" fill="#3fc0f2" opacity=".6"/>
    <circle cx="470" cy="640" r="45" fill="#3fc0f2" opacity=".5"/>
    <circle cx="90" cy="660" r="50" fill="#3fc0f2" opacity=".4"/>
    <rect x="0" y="640" width="548" height="70" fill="#0f5fa8" opacity=".6"/>
  </svg>
  <ul class="perks">
    <li class="perk">
      <div class="perk-tab" style="background:#1c63b5"><svg viewBox="0 0 50 50"><circle cx="25" cy="25" r="22" fill="#fff" stroke="#bbb" stroke-width="3"/><circle cx="25" cy="25" r="16" fill="#1c3f8a"/><path d="M15 18l9 7-9 7zM25 18l9 7-9 7z" fill="#fff"/></svg></div>
      <div class="perk-copy"><h2 class="perk-title">Hate doing laundry?</h2><p class="perk-text">We will fast forward your day with our large commercial washers and dryers. You will be out of here in no time.</p></div>
    </li>
    <li class="perk">
      <div class="perk-tab" style="background:#138a3e"><svg viewBox="0 0 50 50"><circle cx="25" cy="25" r="22" fill="#fff" stroke="#bbb" stroke-width="3"/><circle cx="25" cy="25" r="16" fill="#39b54a"/><text x="25" y="32" text-anchor="middle" font-family="Lato,sans-serif" font-weight="900" font-size="20" fill="#fff">P</text></svg></div>
      <div class="perk-copy"><h2 class="perk-title">Have large laundry loads?</h2><p class="perk-text">Bring them in your car, we have ample parking.</p></div>
    </li>
    <li class="perk">
      <div class="perk-tab" style="background:#c4202e"><svg viewBox="0 0 50 50"><circle cx="25" cy="25" r="22" fill="#fff" stroke="#bbb" stroke-width="3"/><circle cx="25" cy="25" r="16" fill="#e0303c"/><rect x="15" y="17" width="20" height="14" fill="none" stroke="#fff" stroke-width="2"/><path d="M21 35h8" stroke="#fff" stroke-width="2"/></svg></div>
      <div class="perk-copy"><h2 class="perk-title">Get bored doing laundry?</h2><p class="perk-text">Not here! We have free WIFI and flat screen TV to keep you entertained.</p></div>
    </li>
    <li class="perk">
      <div class="perk-tab" style="background:#ee6a1f"><svg viewBox="0 0 50 50"><circle cx="25" cy="25" r="22" fill="#fff" stroke="#bbb" stroke-width="3"/><circle cx="25" cy="25" r="16" fill="#f28a2e"/><path d="M16 22h16v5a8 8 0 0 1-16 0z" fill="#fff"/><path d="M32 24h3v4h-3" fill="none" stroke="#fff" stroke-width="2"/></svg></div>
      <div class="perk-copy"><h2 class="perk-title">Our location is a multi taskers dream:</h2><p class="perk-text">Grocery Shopping at nearby GreenCart. Lunch at LOTUS WOK<br>(OR HOAGIE HUB OR CRISPY COOP), coffee at BEAN HARBOR.</p></div>
    </li>
    <li class="perk">
      <div class="perk-tab" style="background:#8e1f6e"><svg viewBox="0 0 50 50"><circle cx="25" cy="25" r="22" fill="#fff" stroke="#bbb" stroke-width="3"/><circle cx="25" cy="25" r="16" fill="#5b2a86"/><circle cx="25" cy="25" r="10" fill="none" stroke="#fff" stroke-width="2"/><path d="M25 19v6h5" fill="none" stroke="#fff" stroke-width="2"/></svg></div>
      <div class="perk-copy"><h2 class="perk-title">No time for laundry?</h2><p class="perk-text">Bring it to us and collect it washed, folded and neatly packed after 24 hours.</p></div>
    </li>
    <li class="perk">
      <div class="perk-tab" style="background:#7a4a22"><svg viewBox="0 0 50 50"><circle cx="25" cy="25" r="22" fill="#fff" stroke="#bbb" stroke-width="3"/><circle cx="25" cy="25" r="16" fill="#8b5a2b"/><path d="M14 18h4l3 11h12l2-8H19" fill="none" stroke="#fff" stroke-width="2"/><circle cx="22" cy="33" r="1.8" fill="#fff"/><circle cx="31" cy="33" r="1.8" fill="#fff"/></svg></div>
      <div class="perk-copy"><h2 class="perk-title">No time for grocery shopping?</h2><p class="perk-text">Do your grocery shopping at nearby GREENCART while our machines do your laundry.</p></div>
    </li>
    <li class="perk">
      <div class="perk-tab" style="background:#f3e600"><svg viewBox="0 0 50 50"><circle cx="25" cy="25" r="22" fill="#fff" stroke="#bbb" stroke-width="3"/><circle cx="25" cy="25" r="16" fill="#f49a2a"/><path d="M25 13l2 10 10 2-10 2-2 10-2-10-10-2 10-2z" fill="#fff"/></svg></div>
      <div class="perk-copy"><h2 class="perk-title">Tired of washing your clothes<br>in a dirty laundromat?</h2><p class="perk-text">We have the cleanest laundromat in the bay area with efficient attendants.</p></div>
    </li>
  </ul>
  <p class="back-url">www.marlowelaundromat.com</p>
</section>

</body>
</html>
```